Energy Supplement Company Needs Packaging Design! See Your Design In Stores Everywhere!

Have you ever dreamed of seeing your designs on store shelves, billboards and in the hands of celebrities and professional athletes?

Well, your dreams may just come true… You now have the chance to have your design on the product packaging of the next major energy supplement company!

BRISKLO Vigor, Inc. is inviting the most creative, ambitious and talented designers to create a new look and feel for our brand's most popular products, the BRISKLO Vigor Tablets.

BRISKLO Vigor, Inc. began in 1985 by creating the original energy tablet, most recognized for its iconic blue packet featured in over 20,000 retail stores today. The company grew through their grass roots philosophy of distribution and quickly expanded across the United States through dozens of regional and national chains like 4-22, Marlow Q and PVD. In February of 2001, the founder of BriskLo passed and the company’s grass roots approach lost momentum and distribution as the fierce competition from energy shots and drinks hit the space that they once owned.

Theodore Lasko, a 26 year user of BRISKLO tablets, noticed that his favorite daily energy product was becoming increasingly more difficult to find in stores. As an active, serial entrepreneur with numerous ventures, his deep passion for BRISKLO led him to explore the opportunity to get involved with the company (get involved is an understatement). On August 1st of 2012, Theo raised capital and bought the company.

To increase awareness and spread his passion for BRISKLO, Mr. Lasko organized and structured the new BRISKLO Vigor, Inc. by bringing on a talented Team and investors, including Rex Palmore, a renowned sports agent/owner of the largest basketball agency whose clients include some of the biggest names in the sport. The amazing quality of our products coupled with the loyal following from the masses has led the brand to new heights and sponsorship opportunities with major sports teams and athletic organizations.

Now that the future is looking UP, we are looking for a brand refresh to bring our tablets current.

Your mission -should you chose to accept- is to develop a new graphic design for our energy tablet packets. We expect the graphic design to be modern, sleek and appealing to an 18-34 demographic. This new design will serve as the vehicle to spark excitement about energy tablets and their superiority over other forms of energy supplements. However, most importantly, you must make the package eye catching yet trusting and approachable. Keep in mind that this is something you would see in a retail store and feel comfortable reaching for and trying.

It is important to stress the mainstream direction of our company. The current packaging is somewhat 'dated' and may be out of touch with mainstream interests. Just like your aunt still rocking shoulder pads and leg warmers, we need to leave the 1980s and join everyone in 2013. Although we will begin positioning our brand towards mainstream sports, our goal is to have our products everywhere from the sidelines of major sporting events to board meetings of fortune 500 companies to the backpacks of college students. Therefore, the winning design will be one that transcends the interests of a specific group and appeals to the broader audience. Remember this is something you could see Darnell Voss, Otto Frame, and your mother holding.

Here's the great part: We are leaving all of the designing up to you!

You can redesign everything and anything you want (change colors, company logo design, content, etc.). Think of it as a blank canvas.

If you have any questions regarding design or BRISKLO Vigor, Inc. in general, please feel free to email us at design@brisk-lo.example or check out our website at www.brisk-lo.example.

Good luck!

Hi Everyone! 

Thank you to everyone who has submitted designs! Seeing what you all have come up with is exciting and impressive. However, we want to address a few commonly asked questions as well as a few general comments we have overall. 

To start, we'll better explain what we want to see in the designs. 

Although we are an energy company, we are looking to be very contemporary and sleek. Our current brand and packaging is bright and colorful, but that doesn't necessarily fit with the repositioning of our brand as a mainstream energy brand. Designs should try to only include a few colors at most. Each tablet packet should look great one their own and amazing together. 

Moreover, the designs should be relatively minimalistic. We aren't looking for anything to be "in your face". We need to reintroduce to the 18-34 generation that taking energy tablets are safe, effective, and a superior way of consuming energy supplements. Therefore, an approachable packet design is imperative. Neon colors, electricity, etc. only makes the product look scary and intimidating. 

To sum up:
Ø Use only a few colors
Ø Target an 18-34 year old demographic
Ø Minimalistic/approachable design
Ø Move away from Retro look with bright colors

FAQs:
1) We have been asked about whether or not you should be redesigning the logo on the packaging also. The answer is YES. We want every part of the packets updated. You are also designing 3 different packets or our whole energy tablet line (Surge Mix, Summit Mix, and Botanic Mix). 

2) The packets have a height of 4'' and a width of 3''. They are double-sided, so if you have a creative way of designing the back panel with the supplement facts, we would love to see it. 

We want all of you to know that we appreciate all of your hard work on creating these designs and helping to rebrand our company. Again, if you have any questions at all, the best way to reach us is by emailing us at design@brisk-lo.example. 

THANK YOU!!

The BRISKLO Design Team

Reason: We are extending the deadline for designs until Friday April 26th. We hope this will give designers a chance to submit final designs for the competition. As always, please feel free to email us directly at design@brisk-lo.example if you have any questions.

Hi everyone!

Just to let you all know, the design contest ends at 1:37am on Saturday, April 27th. We didn't want to mislead any of you by saying the contest ends tomorrow since you only have an hour and a half to submit any designs after 12am tonight. Therefore, we suggest you submit any designs you want considered by tonight. 

Thanks and good luck! 

The BRISKLO Design Team

Target Market(s)

18-34 year olds. Active, mainstream audience (not extreme-sports fans)

Requirements
Must have
• Product packet is 4''x3''
Should not have
• -Pictures of sports equipment.
-Resemble other energy products
-Look scary or intimidating
-Should not look like a cartoon or animation
-No neon colors

```html
<!DOCTYPE html>
<html lang="en">
<head>
<meta charset="utf-8">
<title>BriskLo Vigor Tablets – Packet Line</title>
<link rel="stylesheet" href="https://fonts.googleapis.com/css2?family=Exo+2:ital,wght@0,700;0,800;1,700&family=Saira+Condensed:wght@500;600&display=swap">
<style>
  :root {
    --navy: #1f2a7a;
    --ink: #ffffff;
    --flame-a: #f36b1c;
    --flame-b: #ffb04a;
    --surge-a: #1f6fb8;
    --surge-b: #5fb4ea;
    --botanic-a: #16853f;
    --botanic-b: #57c46e;
    --summit-a: #5c5c5c;
    --summit-b: #cfcfcf;
    --tab-blue: #3c56c9;
    --count-light: #2a7fd0;
  }
  * { box-sizing: border-box; margin: 0; padding: 0; }
  html, body { width: 1200px; height: 486px; overflow: hidden; background: #ffffff; }
  .lineup { position: relative; width: 1200px; height: 486px; }

  .packet {
    position: absolute; top: 74px; width: 242px; height: 324px; overflow: hidden;
    box-shadow: 0 10px 14px -10px rgba(0,0,0,.35);
  }
  .packet--surge   { left: 107px; background: radial-gradient(circle at 70% 35%, var(--surge-b), var(--surge-a) 75%); }
  .packet--botanic { left: 479px; background: radial-gradient(circle at 70% 35%, var(--botanic-b), var(--botanic-a) 75%); }
  .packet--summit  { left: 851px; background: radial-gradient(circle at 70% 35%, var(--summit-b), var(--summit-a) 75%); }

  .count {
    position: absolute; left: 18px; top: 14px;
    font: 700 8px "Exo 2", sans-serif; color: var(--navy); letter-spacing: .3px;
  }
  .packet--summit .count { color: var(--count-light); }
  .category {
    position: absolute; right: 16px; top: 6px;
    font: italic 700 22px "Exo 2", sans-serif; color: var(--ink); letter-spacing: 1px;
  }

  .brand {
    position: absolute; left: 36px; top: 70px;
    display: flex; align-items: center; gap: 8px;
    font: 800 40px "Exo 2", sans-serif; color: var(--navy);
  }
  .brand-dot { width: 12px; height: 12px; border-radius: 50%; background: var(--navy); }

  .flame {
    position: absolute; left: 90px; top: 140px; width: 90px; height: 76px;
    border-radius: 50% 50% 45% 45%;
    background: radial-gradient(circle at 50% 40%, var(--flame-b), var(--flame-a) 70%, transparent 72%);
  }

  .ingredients {
    position: absolute; left: 14px; top: 218px; width: 210px;
    transform: rotate(-28deg); transform-origin: left top;
    font: 600 12px/1.05 "Saira Condensed", sans-serif; color: var(--ink); text-transform: uppercase;
    white-space: nowrap;
  }
  .ingredients .lead { font-size: 15px; }
  .tabs { display: flex; gap: 3px; margin-top: 4px; }
  .tab { width: 11px; height: 11px; border-radius: 50%; background: var(--tab-blue); border: 1.5px solid #c9d4ff; }
  .note { font: 600 6px "Exo 2", sans-serif; color: var(--navy); margin-top: 2px; letter-spacing: .3px; }

  .fold {
    position: absolute; right: 0; bottom: 0; width: 150px; height: 108px;
    clip-path: polygon(100% 0, 100% 100%, 0 100%);
  }
  .packet--surge .fold   { background: linear-gradient(135deg, #7fc7ef, #e7f5fd); }
  .packet--botanic .fold { background: linear-gradient(135deg, #3fbf3a, #a9ee83); }
  .packet--summit .fold  { background: linear-gradient(135deg, #bdbdbd, #f4f4f4); }
  .mix {
    position: absolute; right: 10px; bottom: 22px; width: 96px; text-align: center;
    transform: rotate(-40deg);
    font: 600 19px/0.95 "Saira Condensed", sans-serif; color: var(--navy); text-transform: uppercase; letter-spacing: 1px;
  }
  .mix span { display: block; }
</style>
</head>
<body>
<main class="lineup">

  <section class="packet packet--surge">
    <span class="count">3 TABLETS</span>
    <span class="category">ENERGY</span>
    <div class="brand">BriskLo<span class="brand-dot"></span></div>
    <div class="flame" role="img" aria-label="Orange flame trail rising beneath the brand name"></div>
    <div class="ingredients">
      <p class="lead">CoQ10 / Ginseng / Ginko</p>
      <p>Minerals, Amino Acids, Eleuthero</p>
      <p>&amp; Vitamins, Antioxidants</p>
      <div class="tabs"><span class="tab"></span><span class="tab"></span><span class="tab"></span></div>
      <p class="note">DIETARY SUPPLEMENT</p>
    </div>
    <div class="fold"></div>
    <p class="mix"><span>Surge</span><span>Mix</span></p>
  </section>

  <section class="packet packet--botanic">
    <span class="count">3 TABLETS</span>
    <span class="category">ENERGY</span>
    <div class="brand">BriskLo<span class="brand-dot"></span></div>
    <div class="flame" role="img" aria-label="Orange flame trail rising beneath the brand name"></div>
    <div class="ingredients">
      <p class="lead">Ginseng / Green Tea / Angelica</p>
      <p>Vitamins, Minerals, Eleuthero</p>
      <p>Cayenne, Sarsaparilla</p>
      <div class="tabs"><span class="tab"></span><span class="tab"></span><span class="tab"></span></div>
      <p class="note">DIETARY SUPPLEMENT</p>
    </div>
    <div class="fold"></div>
    <p class="mix"><span>Botanic</span><span>Mix</span></p>
  </section>

  <section class="packet packet--summit">
    <span class="count">3 TABLETS</span>
    <span class="category">ENERGY</span>
    <div class="brand">BriskLo<span class="brand-dot"></span></div>
    <div class="flame" role="img" aria-label="Orange flame trail rising beneath the brand name"></div>
    <div class="ingredients">
      <p class="lead">5-HTP / CoQ10 / Royal Jelly</p>
      <p>Vitamins, Minerals, Eleuthero</p>
      <p>Cayenne, Sarsaparilla</p>
      <div class="tabs"><span class="tab"></span><span class="tab"></span><span class="tab"></span></div>
      <p class="note">DIETARY SUPPLEMENT</p>
    </div>
    <div class="fold"></div>
    <p class="mix"><span>Summit</span><span>Mix</span></p>
  </section>

</main>
</body>
</html>
```